I m Looking to Demonstrate My Product Features via Design & Elements

My Dear Freinds,

I am looking to demonstrate the following features of my product via design & elements (for my Brindlemart listing)
https://www.brindlemart.example/dp/X72QP4LWZN/ref=kvt_h_3_u

1) Soft Touch - Skin Friendly Silky Soft Lining Inner Brushed Fleece

2) Stretchable - Four-way Stretch for Unrestricted Movement

3) Breathable - Moisture Control Odor Resistant

4) Quick-Drying - Sweat Wicking and Quick Dry Performance

5) Moisture-Wicking - Excellent Mobility and Moisture-Wicking

6) Heat Retention - Excellent Thermal Retention

7) Ultra-Light & Comfortable for Daily Warmth

8) Wonderfully Warm - Extra Layer of Warmth Under Your Clothes,

9) Elastic waistband - For the Pants for a Comfortable Snug Fit

10) Shrinkage Controlled - For lasting size and shape

see attached some examples & ideas

P.S. it shouldn't be exactly the same because these are from my competitors

Target Market(s)

People on Brindlemart who are looking to buy Thermal Underwear

Industry/Entity Type

Womens Clothing

Font styles to use
Serif

Colors

Designer to choose colors to be used in the design.

Requirements
Must have
• Needs to be attractive
Nice to have
• Ok
Should not have
• Ok

```html
<!DOCTYPE html>
<html lang="en">
<head>
<meta charset="utf-8">
<title>Thermal Set Features</title>
<link href="https://fonts.googleapis.com/css2?family=Playfair+Display:wght@700&family=Lora:wght@400;600&display=swap" rel="stylesheet">
<style>
  :root {
    --page: #f6f1ea;
    --navy: #1f2a4d;
    --ink: #2b2b33;
    --muted: #5b5d6b;
    --accent: #3f9fd3;
    --accent-deep: #2a78a8;
    --icon-bg: #e3eef7;
    --rule: #d9d1c4;
    --card: #ffffff;
  }
  * { margin: 0; padding: 0; box-sizing: border-box; }
  html, body { width: 1200px; height: 784px; overflow: hidden; }
  body {
    position: relative;
    background: var(--page);
    font-family: "Lora", serif;
    color: var(--ink);
  }

  /* Left: product visual */
  .product-photo {
    position: absolute;
    left: 30px; top: 30px;
    width: 420px; height: 724px;
    border-radius: 24px;
    background: linear-gradient(160deg, #eaf1f6 0%, #cfe3f1 45%, var(--accent) 100%);
  }
  .fabric-detail {
    position: absolute;
    left: 300px; top: 400px;
    width: 130px; height: 130px;
    border-radius: 50%;
    background: radial-gradient(circle at 40% 40%, #5bb6e4, var(--accent) 55%, var(--accent-deep));
    border: 4px solid var(--card);
    outline: 2px dotted var(--navy);
    outline-offset: 4px;
  }
  .set-card {
    position: absolute;
    left: 54px; top: 560px;
    width: 372px;
    padding: 20px 24px;
    background: var(--card);
    border-radius: 16px;
    box-shadow: 0 8px 24px rgba(31, 42, 77, 0.15);
  }
  .set-card-title {
    font-family: "Playfair Display", serif;
    font-weight: 700;
    font-size: 22px;
    color: var(--navy);
    margin-bottom: 8px;
  }
  .set-card-text {
    font-size: 15px;
    line-height: 23px;
    color: var(--muted);
  }

  /* Right: feature grid */
  .feature-grid {
    position: absolute;
    left: 490px; top: 30px;
    width: 680px; height: 724px;
    display: grid;
    grid-template-columns: 1fr 1fr;
    grid-template-rows: repeat(5, 1fr);
    column-gap: 32px;
  }
  .feature {
    display: flex;
    align-items: center;
    gap: 18px;
    border-bottom: 1px solid var(--rule);
  }
  .feature:nth-last-child(-n+2) { border-bottom: none; }
  .feature-icon {
    flex: 0 0 58px;
    width: 58px; height: 58px;
    border-radius: 50%;
    background: var(--icon-bg);
    display: flex; align-items: center; justify-content: center;
  }
  .feature-icon svg { width: 34px; height: 34px; }
  .feature-title {
    font-family: "Playfair Display", serif;
    font-weight: 700;
    font-size: 19px;
    line-height: 25px;
    color: var(--navy);
  }
  .feature-text {
    font-size: 14.5px;
    line-height: 21px;
    color: var(--muted);
    margin-top: 3px;
  }
</style>
</head>
<body>

  <div class="product-photo" role="img" aria-label="Woman resting on a white bed wearing the blue two piece thermal set"></div>
  <div class="fabric-detail" role="img" aria-label="Close-up of the blue fleece lined fabric"></div>

  <div class="set-card">
    <div class="set-card-title">2 PIECE SET:</div>
    <div class="set-card-text">These Kestrel thermals are designed for comfort with an elastic waistband and fleece lined moisture wicking microfibers. They are stretchy comfortable.</div>
  </div>

  <div class="feature-grid">
    <div class="feature">
      <div class="feature-icon">
        <svg viewBox="0 0 64 64" fill="none" stroke="var(--navy)" stroke-width="4" stroke-linecap="round" stroke-linejoin="round">
          <path d="M20 26a12 12 0 1 1 24 0"/>
          <path d="M30 58V24a3 3 0 0 1 6 0v14l8 2a4 4 0 0 1 3 5l-2 13z" fill="var(--navy)"/>
        </svg>
      </div>
      <div>
        <div class="feature-title">Soft Touch</div>
        <div class="feature-text">Skin Friendly Silky Soft Lining Inner Brushed Fleece</div>
      </div>
    </div>

    <div class="feature">
      <div class="feature-icon">
        <svg viewBox="0 0 64 64" fill="none" stroke="var(--navy)" stroke-width="4" stroke-linecap="round">
          <path d="M6 16h52M6 32h52M6 48h52"/>
          <path d="M16 6v52M32 6v52M48 6v52" stroke-dasharray="7 6"/>
        </svg>
      </div>
      <div>
        <div class="feature-title">Stretchable</div>
        <div class="feature-text">Four-way Stretch for Unrestricted Movement</div>
      </div>
    </div>

    <div class="feature">
      <div class="feature-icon">
        <svg viewBox="0 0 64 64" fill="none" stroke="var(--navy)" stroke-width="4" stroke-linecap="round" stroke-linejoin="round">
          <path d="M32 4v24M32 26l-8 8M32 26l8 8"/>
          <path d="M24 18c-10 2-18 18-18 36l14-4 4-10z"/>
          <path d="M40 18c10 2 18 18 18 36l-14-4-4-10z"/>
        </svg>
      </div>
      <div>
        <div class="feature-title">Breathable</div>
        <div class="feature-text">Moisture Control Odor Resistant</div>
      </div>
    </div>

    <div class="feature">
      <div class="feature-icon">
        <svg viewBox="0 0 64 64" fill="none" stroke="var(--navy)" stroke-width="4" stroke-linecap="round" stroke-linejoin="round">
          <path d="M16 12h16l6 10-4 2v22H14V24l-4-2z" fill="var(--navy)"/>
          <path d="M42 36h18M42 44h18M42 52h18"/>
        </svg>
      </div>
      <div>
        <div class="feature-title">Quick-Drying</div>
        <div class="feature-text">Sweat Wicking and Quick Dry Performance</div>
      </div>
    </div>

    <div class="feature">
      <div class="feature-icon">
        <svg viewBox="0 0 64 64" fill="none" stroke="var(--navy)" stroke-width="4" stroke-linecap="round" stroke-linejoin="round">
          <path d="M32 6C22 20 16 28 16 38a16 16 0 0 0 32 0c0-10-6-18-16-32z"/>
          <path d="M24 40a8 8 0 0 0 8 8"/>
        </svg>
      </div>
      <div>
        <div class="feature-title">Moisture-Wicking</div>
        <div class="feature-text">Excellent Mobility and Moisture-Wicking</div>
      </div>
    </div>

    <div class="feature">
      <div class="feature-icon">
        <svg viewBox="0 0 64 64" fill="none" stroke="var(--navy)" stroke-width="4" stroke-linecap="round">
          <path d="M22 8a5 5 0 0 1 10 0v30a11 11 0 1 1-10 0z"/>
          <circle cx="27" cy="48" r="4" fill="var(--navy)"/>
          <path d="M27 18v26M44 16h12M44 26h8"/>
        </svg>
      </div>
      <div>
        <div class="feature-title">Heat Retention</div>
        <div class="feature-text">Excellent Thermal Retention</div>
      </div>
    </div>

    <div class="feature">
      <div class="feature-icon">
        <svg viewBox="0 0 64 64" fill="none" stroke="var(--navy)" stroke-width="4" stroke-linecap="round" stroke-linejoin="round">
          <path d="M32 52C16 40 10 32 14 24s14-6 18 2c4-8 14-10 18-2s-2 16-18 28z"/>
        </svg>
      </div>
      <div>
        <div class="feature-title">Ultra-Light &amp; Comfortable for Daily Warmth</div>
      </div>
    </div>

    <div class="feature">
      <div class="feature-icon">
        <svg viewBox="0 0 64 64" fill="none" stroke="var(--navy)" stroke-width="4" stroke-linecap="round">
          <circle cx="32" cy="32" r="12"/>
          <path d="M32 4v8M32 52v8M4 32h8M52 32h8M12 12l6 6M46 46l6 6M12 52l6-6M46 18l6-6"/>
        </svg>
      </div>
      <div>
        <div class="feature-title">Wonderfully Warm</div>
        <div class="feature-text">Extra Layer of Warmth Under Your Clothes,</div>
      </div>
    </div>

    <div class="feature">
      <div class="feature-icon">
        <svg viewBox="0 0 64 64" fill="none" stroke="var(--navy)" stroke-width="4" stroke-linecap="round" stroke-linejoin="round">
          <path d="M32 4v14M26 12l6 6 6-6"/>
          <path d="M32 60V46M26 52l6-6 6 6"/>
          <path d="M4 28q28-10 56 0M4 38q28-10 56 0"/>
        </svg>
      </div>
      <div>
        <div class="feature-title">Elastic waistband</div>
        <div class="feature-text">For the Pants for a Comfortable Snug Fit</div>
      </div>
    </div>

    <div class="feature">
      <div class="feature-icon">
        <svg viewBox="0 0 64 64" fill="none" stroke="var(--navy)" stroke-width="4" stroke-linecap="round" stroke-linejoin="round">
          <path d="M32 4v14M25 11l7 7 7-7"/>
          <path d="M32 60V46M25 53l7-7 7 7"/>
          <path d="M8 27h48M8 37h48"/>
        </svg>
      </div>
      <div>
        <div class="feature-title">Shrinkage Controlled</div>
        <div class="feature-text">For lasting size and shape</div>
      </div>
    </div>
  </div>

</body>
</html>
```